New Toothpaste brand needs a logo & packaging design

Our company is launching a new toothpaste and is looking for a logo and packaging design. The toothpaste brand is called Brivana. The packaging should have the same design quality as the major international brands, such as Lumora, Lumora Totalcare, Dentiva, Pexolo, Wind-rise, Marvest, etc. The dominant colors for our brand should be hues of blue, similar to other major brands. In addition, there should be a little bit of green to represent the "Fresh Mint Blast" flavor and the "Extracts of Aloe Vera" included in the ingredients.

There are typically 3 unique sides on a toothpaste box:

The face: Repeated on ~3 sides of the 4 faces of the box
The back: The 4th box face has the instructions for use, ingredients, company information, bar code/product info, and some branding elements.
The sides: Usually consisting of just the logo, flavor etc.

Please refer to existing brands such as Lumora, Lumora Total-care, and Dentiva for an example of typical box layout and elements.

Task Details:
Package Dimensions: 180 mm x 48 mm x 28 mm, 100 ml toothpaste tube
Brand Name: Brivana
Description: Fluoride Toothpaste
Flavor: Fresh Mint Blast
5 Actions: Protects against cavities and tartar, freshens breath, whitens teeth, and maintains healthy gums. These actions can also be made into a list like Lumora Total Care or Dentiva Max care. For instance, Strong Teeth, Fresh Breath, Whitening, Healthy Gums, Cavity and Tartar Protection.
Also contains whitening micro particles and extracts of aloe vera which may be highlighted on the package

Overall, the look should be high quality and with the same look and feel as the big brands mentioned previously. We do not have an existing logo for this brand. The face of the package is the most important element as it is often repeated on several sides and on the tube itself.

Please let me know if you have any questions.

I've attached some of our favorite big brand designs below. I would say the Lumora Total Care and Gleam vers

The logos I've seen so far for Brivana, have been a bit too bold. A little bold is okay, but just needs to be moderate. 

I would like the colors to be bright and appealing. I mentioned shades of blue being the major color, but green should also be highlighted as well, perhaps in a 80% blue to 20% green ratio. 

Target Market(s)

adult consumer of toothpaste, both female and male.

Industry/Entity Type

It Company

Requirements
Must have
• A logo with the brand name: Brivana
Description or sub text: Fluoride Toothpaste
Flavor: Fresh Mint Blast
A phrase or list describing the Toothpaste Actions: e.g., Protects against cavities and tartar, freshens breath, whitens teeth, and maintains healthy gums. Or as a list simialr to Lumora Total Care or Dentiva Max Care:
-Anti-cavity
-Anti-tartar
-Fresh breath
-Whitening
-Healthy Gums

Special ingredient of "whitening micro particles: and "extracts of aloe vera", which should also be highlighted.

The color should mostly be shades of blue, with only a little bit of green to accentuate the fresh mint blast flavor and aloe vera

Nice to have
• The design should really look good next to lumora total care, gleam pure, and dentiva max care. These are our favorite designs.
Should not have
• For aloe vera, there is no need to show the plant.

The Brivana logo shouldn't be too Bold. This should be appeal to all consumers, not just men.

```html
<!DOCTYPE html>
<html lang="en">
<head>
<meta charset="UTF-8">
<title>Brivana Fluoride Toothpaste – Packaging Faces</title>
<link href="https://fonts.googleapis.com/css2?family=Open+Sans:ital,wght@0,700;1,700;1,800&display=swap" rel="stylesheet">
<style>
  :root {
    --page-bg: #eceef0;
    --navy: #071a4a;
    --deep-blue: #0a3a9a;
    --bright-blue: #1a6fe0;
    --cyan: #3fd6f2;
    --ice: #bff3ff;
    --mint: #5fe3a1;
    --mint-deep: #17a866;
    --white: #ffffff;
    --band: #0b2f86;
    --band-line: #4aa8ff;
  }
  * { margin: 0; padding: 0; box-sizing: border-box; }
  html, body {
    width: 1200px; height: 1200px; overflow: hidden;
    background: var(--page-bg);
    font-family: "Open Sans", Arial, sans-serif;
  }

  /* shared face artwork */
  .pack-face {
    position: absolute; left: 50px; width: 1100px;
    overflow: hidden; color: var(--white);
    background: linear-gradient(100deg, var(--navy) 0%, var(--deep-blue) 32%, var(--bright-blue) 58%, var(--deep-blue) 84%, var(--navy) 100%);
  }
  .sparkle-field {
    position: absolute; inset: 0;
    background:
      radial-gradient(ellipse 40% 55% at 46% 38%, rgba(63,214,242,0.55), transparent 70%),
      radial-gradient(ellipse 22% 45% at 70% 70%, rgba(95,227,161,0.35), transparent 70%),
      radial-gradient(ellipse 28% 40% at 84% 30%, rgba(63,214,242,0.25), transparent 70%),
      radial-gradient(ellipse 25% 50% at 28% 70%, rgba(26,111,224,0.5), transparent 70%);
  }
  .brand-mark {
    position: absolute; left: 40px; top: 0;
    display: flex; align-items: center; gap: 14px;
  }
  .brand-dot { border-radius: 50%; background: var(--white); flex: none; }
  .brand-name { font-weight: 700; font-style: normal; color: var(--white); letter-spacing: 1px; }
  .product-copy {
    position: absolute; right: 40px;
    text-align: center; font-style: italic;
  }
  .product-title { font-weight: 800; line-height: 1.1; letter-spacing: 0.5px; }
  .flavor { font-weight: 800; color: var(--mint); }
  .claims { font-weight: 700; line-height: 1.3; text-transform: uppercase; }
  .ingredient-chips {
    display: flex; justify-content: center; gap: 12px; list-style: none;
  }
  .ingredient-chips li {
    display: flex; align-items: center; gap: 8px;
    font-style: normal; font-weight: 700; text-transform: uppercase;
    border-radius: 999px; letter-spacing: 0.5px;
  }
  .chip-aloe { background: var(--mint-deep); }
  .chip-white { background: rgba(255,255,255,0.18); border: 1px solid var(--ice); }
  .chip-aloe::before, .chip-white::before {
    content: ""; width: 8px; height: 8px; border-radius: 50%;
  }
  .chip-aloe::before { background: var(--white); }
  .chip-white::before { background: var(--ice); }
  .benefit-band {
    position: absolute; left: 0; right: 0; bottom: 0;
    background: linear-gradient(90deg, var(--navy), var(--band) 40%, var(--band));
    border-top: 2px solid var(--band-line);
    display: flex; align-items: center; justify-content: flex-end;
    padding-right: 40px;
  }
  .benefit-list {
    display: flex; list-style: none;
    font-weight: 700; color: var(--white);
    text-transform: uppercase; letter-spacing: 0.5px;
  }
  .benefit-list li + li::before { content: "|"; margin: 0 9px; color: var(--mint); }

  /* side face (top of box) */
  .side-face { top: 110px; height: 170px; }
  .side-face .brand-mark { bottom: 30px; }
  .side-face .brand-dot { width: 22px; height: 22px; }
  .side-face .brand-name { font-size: 40px; }
  .side-face .product-copy { left: 400px; top: 14px; }
  .side-face .product-title { font-size: 27px; }
  .side-face .flavor { font-size: 18px; margin-top: 2px; }
  .side-face .claims { font-size: 13px; margin-top: 8px; }
  .side-face .benefit-band { height: 30px; }
  .side-face .benefit-list { font-size: 12px; }

  /* front face */
  .front-face { top: 310px; height: 294px; }
  .front-face .brand-mark { bottom: 44px; }
  .front-face .brand-dot { width: 34px; height: 34px; }
  .front-face .brand-name { font-size: 60px; }
  .front-face .product-copy { left: 420px; top: 20px; }
  .front-face .product-title { font-size: 40px; }
  .front-face .flavor { font-size: 28px; margin-top: 2px; }
  .front-face .claims { font-size: 18px; margin-top: 10px; }
  .front-face .ingredient-chips { margin-top: 10px; }
  .front-face .ingredient-chips li { font-size: 13px; padding: 4px 14px; }
  .front-face .benefit-band { height: 44px; }
  .front-face .benefit-list { font-size: 16px; }

  /* tube face, flattened */
  .tube-face { top: 650px; height: 300px; }
  .tube-face .brand-mark { bottom: 40px; left: 50px; }
  .tube-face .brand-dot { width: 30px; height: 30px; }
  .tube-face .brand-name { font-size: 54px; }
  .tube-face .product-copy { left: 400px; right: 110px; top: 22px; }
  .tube-face .product-title { font-size: 38px; }
  .tube-face .flavor { font-size: 26px; margin-top: 2px; }
  .tube-face .claims { font-size: 17px; margin-top: 10px; }
  .tube-face .ingredient-chips { margin-top: 12px; }
  .tube-face .ingredient-chips li { font-size: 12px; padding: 4px 12px; }
  .tube-face .benefit-band { height: 40px; padding-right: 110px; }
  .tube-face .benefit-list { font-size: 14px; }
  .tube-crimp {
    position: absolute; right: 0; top: 0; bottom: 0; width: 60px;
    background: repeating-linear-gradient(90deg, #0a2a78 0 4px, #123c9c 4px 8px);
    border-left: 2px solid var(--band-line);
  }
</style>
</head>
<body>
  <section class="pack-face side-face">
    <div class="sparkle-field" role="img" aria-label="Blue, cyan and mint sparkle particle burst background"></div>
    <div class="brand-mark"><span class="brand-dot"></span><span class="brand-name">Brivana</span></div>
    <div class="product-copy">
      <h2 class="product-title">FLUORIDE TOOTHPASTE</h2>
      <p class="flavor">FRESH MINT BLAST</p>
      <p class="claims">Protects against cavities and tartar, freshens breath, whitens teeth, and<br>maintains healthy gums</p>
    </div>
    <div class="benefit-band">
      <ul class="benefit-list"><li>Anti-cavity</li><li>Anti-tartar</li><li>Fresh breath</li><li>Whitening</li><li>Healthy gums</li></ul>
    </div>
  </section>

  <section class="pack-face front-face">
    <div class="sparkle-field" role="img" aria-label="Blue, cyan and mint sparkle particle burst background"></div>
    <div class="brand-mark"><span class="brand-dot"></span><span class="brand-name">Brivana</span></div>
    <div class="product-copy">
      <h1 class="product-title">FLUORIDE TOOTHPASTE</h1>
      <p class="flavor">FRESH MINT BLAST</p>
      <p class="claims">Protects against cavities and tartar,<br>freshens breath, whitens teeth, and<br>maintains healthy gums</p>
      <ul class="ingredient-chips">
        <li class="chip-white">Whitening micro particles</li>
        <li class="chip-aloe">Extracts of aloe vera</li>
      </ul>
    </div>
    <div class="benefit-band">
      <ul class="benefit-list"><li>Anti-cavity</li><li>Anti-tartar</li><li>Fresh breath</li><li>Whitening</li><li>Healthy gums</li></ul>
    </div>
  </section>

  <section class="pack-face tube-face">
    <div class="sparkle-field" role="img" aria-label="Blue, cyan and mint sparkle particle burst background"></div>
    <div class="brand-mark"><span class="brand-dot"></span><span class="brand-name">Brivana</span></div>
    <div class="product-copy">
      <h2 class="product-title">FLUORIDE TOOTHPASTE</h2>
      <p class="flavor">FRESH MINT BLAST</p>
      <p class="claims">Protects against cavities and tartar,<br>freshens breath, whitens teeth, and<br>maintains healthy gums</p>
      <ul class="ingredient-chips">
        <li class="chip-white">Whitening micro particles</li>
        <li class="chip-aloe">Extracts of aloe vera</li>
      </ul>
    </div>
    <div class="benefit-band">
      <ul class="benefit-list"><li>Anti-cavity</li><li>Anti-tartar</li><li>Fresh breath</li><li>Whitening</li><li>Healthy gums</li></ul>
    </div>
    <div class="tube-crimp"></div>
  </section>
</body>
</html>
```